Almond butter sachet and jar for new brand called Fenwick’s Pantry

Design for the front and back of a Almond butter sachet and jar, premium design aimed at the fitness market but still approachable for non gym goers.
The Brand name is Fenwick’s Pantry,
Martin Hale is the founder and a michelin starred chef. We want this to stand out from the crowd as a luxury, natural product for use in the gym as well as on the go, we like the premium look of black as a base colour and red colours as they don’t exist in the market, however they can be a little too bold, Our product is natural with no additives, it is vegan, paleo, keto, friendly, plant based and gluten free and only uses hi-Oleic Nuts and no sweetness or palm oil.
Pictures below of the dot&seed sachet and jar are the exact same style as our sachet and jar. The other product is one we really like the look of which is aimed at the fitness market, we don’t want to be the same but almost a hybrid of the two. Our target market however is the high end fitness community, especially with the sachet.

Target Market(s)

Health and Fitness

Requirements
Must have
• High end look and feel,
Nice to have
• Any unique touches to make it stand out from the crowd

```html
<!DOCTYPE html>
<html lang="en">
<head>
<meta charset="utf-8">
<title>Fenwick’s Pantry – Smooth Almond Butter Sachet</title>
<link href="https://fonts.googleapis.com/css2?family=Kalam:wght@400;700&display=swap" rel="stylesheet">
<style>
  :root {
    --page-bg: #ffffff;
    --brown: #6a3e1b;
    --brown-dark: #5b3315;
    --white: #ffffff;
    --silver-top: #c6c6c6;
    --silver-mid: #a4a4a4;
    --silver-light: #e6e6e6;
    --silver-low: #bdbdbd;
    --arch-light: #d9dbdc;
    --glow-warm: #f1d9b0;
    --almond-light: #efbb62;
    --almond-mid: #d98f34;
    --almond-glow: #f2a640;
  }
  * { margin: 0; padding: 0; box-sizing: border-box; }
  html, body {
    width: 1200px;
    height: 820px;
    overflow: hidden;
    background: var(--page-bg);
  }
  .canvas {
    position: relative;
    width: 1200px;
    height: 820px;
  }
  .sachet-front {
    position: absolute;
    left: 378px;
    top: 30px;
    width: 444px;
    height: 760px;
    overflow: hidden;
    background: linear-gradient(180deg,
      var(--silver-top) 0%,
      var(--silver-mid) 30%,
      #b8b8b8 45%,
      var(--silver-light) 68%,
      #dcdcdc 80%,
      var(--silver-low) 100%);
    box-shadow: 6px 8px 14px rgba(0, 0, 0, 0.25);
    font-family: "Kalam", cursive;
  }
  .top-arch {
    position: absolute;
    left: 0;
    top: 0;
    width: 444px;
    height: 190px;
  }
  .brand-name {
    position: absolute;
    left: 0;
    width: 100%;
    top: 122px;
    text-align: center;
    font-size: 32px;
    font-weight: 400;
    color: var(--brown);
    line-height: 1;
  }
  .almond-art {
    position: absolute;
    left: 0;
    top: 0;
    width: 444px;
    height: 760px;
  }
  .product-title {
    position: absolute;
    left: 72px;
    top: 212px;
    color: var(--brown);
    line-height: 0.9;
  }
  .product-title .variant {
    display: block;
    margin-left: 98px;
    font-size: 56px;
    font-weight: 700;
    color: var(--white);
    line-height: 0.9;
  }
  .product-title .name {
    display: block;
    font-size: 106px;
    font-weight: 700;
    letter-spacing: -3px;
    line-height: 0.92;
  }
  .product-title .name.second { margin-left: 8px; }
  .pack-type {
    position: absolute;
    right: 56px;
    top: 552px;
    text-align: right;
    font-size: 42px;
    font-weight: 400;
    color: var(--brown);
    line-height: 0.95;
  }
  .pack-type span { display: block; }
  .weight-tab {
    position: absolute;
    left: 196px;
    top: 634px;
    width: 131px;
    height: 126px;
    background: var(--brown-dark);
    border-radius: 66px 66px 0 0;
    color: var(--white);
    text-align: center;
    font-size: 32px;
    font-weight: 400;
    padding-top: 20px;
  }
</style>
</head>
<body>
<div class="canvas">
  <section class="sachet-front">
    <svg class="top-arch" viewBox="0 0 444 190" aria-hidden="true">
      <defs>
        <radialGradient id="archGlow" cx="0.5" cy="0" r="0.75">
          <stop offset="0" stop-color="var(--glow-warm)"/>
          <stop offset="0.55" stop-color="var(--arch-light)"/>
          <stop offset="1" stop-color="#c4c6c7"/>
        </radialGradient>
      </defs>
      <path d="M0 0 H444 V40 C430 130 340 185 222 185 C104 185 14 130 0 40 Z" fill="url(#archGlow)"/>
    </svg>

    <p class="brand-name">Fenwick’s Pantry</p>

    <svg class="almond-art" viewBox="0 0 444 760" role="img" aria-label="Illustration area: a whole almond at lower left and a blurred almond at the right edge">
      <defs>
        <radialGradient id="almondArea" cx="0.5" cy="0.5" r="0.5">
          <stop offset="0" stop-color="var(--almond-light)"/>
          <stop offset="0.6" stop-color="var(--almond-mid)" stop-opacity="0.85"/>
          <stop offset="1" stop-color="var(--almond-mid)" stop-opacity="0"/>
        </radialGradient>
        <radialGradient id="blurArea" cx="0.5" cy="0.5" r="0.5">
          <stop offset="0" stop-color="var(--almond-glow)" stop-opacity="0.85"/>
          <stop offset="1" stop-color="var(--almond-glow)" stop-opacity="0"/>
        </radialGradient>
      </defs>
      <rect x="330" y="360" width="200" height="320" fill="url(#blurArea)"/>
      <rect x="0" y="470" width="280" height="285" fill="url(#almondArea)"/>
    </svg>

    <h1 class="product-title">
      <span class="variant">Smooth</span>
      <span class="name">Almond</span>
      <span class="name second">Butter</span>
    </h1>

    <p class="pack-type"><span>Squeeze</span><span>pack</span></p>

    <div class="weight-tab">30 gm</div>
  </section>
</div>
</body>
</html>
```